Food home delivery flyer to attract new customers and drive web traffic

We need a flyer for Grubella Home Delivery for our door to door leaflet drop. The aim of our marketing is to attract new customers by driving traffic to our website and raise awareness of our service.

We want the flyer in A5, double sided, and in colour. This campaign will be primarily in print, but we need a PDF option also.

Please visit www.grubellahomedelivery.example to obtain a real feel of who we are and what we do.

The flyer should contain the Grubella Home Delivery logo, with our images to compliment our service and what we offer. All are attached to this brief, along with what wording we expect to be included in the flyer.

The main points we need to shout about are:
Sourcing fresh produce from local growers
Partnering with local businesses
Friendly team offering superior customer service
Fast, safe home delivery
Sustainable business

```html
<!DOCTYPE html>
<html lang="en">
<head>
<meta charset="utf-8">
<title>Grubella Home Delivery – July Offer Flyer</title>
<link rel="stylesheet" href="https://fonts.googleapis.com/css2?family=Montserrat:wght@400;500;700;800&display=swap">
<style>
  :root {
    --page-bg: #ffffff;
    --forest: #0e6133;
    --lime: #93bc2b;
    --ink: #1a1a1a;
    --white: #ffffff;
    --offer-panel: rgba(38, 38, 34, 0.78);
  }
  * { margin: 0; padding: 0; box-sizing: border-box; }
  html, body {
    width: 929px; height: 1200px; overflow: hidden;
    background: var(--page-bg);
    font-family: "Montserrat", Arial, sans-serif;
    color: var(--ink);
  }
  .flyer {
    position: absolute; left: 57px; top: 72px;
    width: 810px; height: 1050px;
    background: var(--white);
    overflow: hidden;
    box-shadow: 0 2px 10px rgba(0,0,0,0.18);
  }
  .flyer-art { position: absolute; inset: 0; }
  .brand {
    position: absolute; left: 29px; top: 38px;
    color: var(--white); font-weight: 700;
    line-height: 1;
  }
  .brand-name { font-size: 46px; letter-spacing: -0.5px; display: block; }
  .brand-sub { font-size: 17px; display: block; margin-top: 6px; margin-left: 4px; }
  .intro {
    position: absolute; left: 41px; top: 164px; width: 318px;
    font-size: 14px; line-height: 19px; text-align: justify;
  }
  .order {
    position: absolute; left: 41px; top: 241px; width: 330px;
    font-size: 15.5px; line-height: 20px;
  }
  .order .url { font-weight: 800; font-size: 14.5px; }
  .order .note { font-size: 13.5px; }
  .body-copy {
    position: absolute; left: 41px; width: 318px;
    font-size: 12.6px; line-height: 17.5px; text-align: justify;
  }
  .body-copy.about { top: 324px; }
  .body-copy.green { top: 446px; }
  .promo {
    position: absolute; left: 40px; top: 526px;
    font-size: 33px; line-height: 44px; font-weight: 500;
  }
  .promo .code { color: var(--forest); font-weight: 800; display: block; }
  .offer {
    position: absolute; left: 440px; top: 355px; width: 335px; height: 146px;
    background: var(--offer-panel); color: var(--white);
    text-align: center;
  }
  .offer-big { font-size: 36px; font-weight: 800; line-height: 1; display: block; }
  .offer-big.first { margin-top: 17px; }
  .offer-line { font-size: 19.5px; font-weight: 500; display: block; margin: 6px 0 5px; }
  .cta {
    position: absolute; left: 0; right: 0; top: 870px;
    text-align: center; color: var(--white);
  }
  .cta-head { font-size: 25px; font-weight: 800; display: block; line-height: 32px; }
  .cta-url { font-size: 26px; font-weight: 800; display: block; line-height: 34px; }
  .cta-call { font-size: 16.5px; font-weight: 400; display: block; margin-top: 6px; line-height: 22px; }
  .cta-phone { font-size: 38px; font-weight: 800; display: block; line-height: 46px; }
</style>
</head>
<body>
<main class="flyer">
  <svg class="flyer-art" width="810" height="1050" viewBox="0 0 810 1050" aria-hidden="false">
    <defs>
      <linearGradient id="hero-tones" x1="0" y1="0" x2="0.3" y2="1">
        <stop offset="0" stop-color="#9a8360"/>
        <stop offset="0.35" stop-color="#8aa05a"/>
        <stop offset="0.65" stop-color="#6d6a4a"/>
        <stop offset="1" stop-color="#c98a45"/>
      </linearGradient>
      <linearGradient id="platter-tones" x1="0" y1="0" x2="1" y2="1">
        <stop offset="0" stop-color="#e9e2da"/><stop offset="1" stop-color="#d46a55"/>
      </linearGradient>
      <linearGradient id="veg-tones" x1="0" y1="0" x2="1" y2="1">
        <stop offset="0" stop-color="#5f9a3a"/><stop offset="0.5" stop-color="#c8462e"/><stop offset="1" stop-color="#6c3e5e"/>
      </linearGradient>
      <linearGradient id="pizza-tones" x1="0" y1="0" x2="1" y2="1">
        <stop offset="0" stop-color="#d8542f"/><stop offset="1" stop-color="#b2532a"/>
      </linearGradient>
    </defs>

    <path class="brand-band" d="M0,30 L300,24 L322,60 L334,100 L320,128 L200,140 L0,138 Z" fill="var(--forest)"/>

    <path class="hero-photo" role="img" aria-label="Photo of picnic box foods: savoury tarts, scotch eggs and roasted squash quinoa salad"
          d="M544,0 L810,0 L810,640 Q650,720 490,743 Q400,620 410,400 Q420,150 544,0 Z" fill="url(#hero-tones)"/>

    <path class="lime-wave" d="M0,655 C150,740 330,770 480,752 C620,735 720,690 810,640 L810,1050 L0,1050 Z" fill="var(--lime)"/>

    <circle cx="200" cy="762" r="90" fill="var(--white)"/>
    <circle class="photo-platter" role="img" aria-label="Photo of a sharing platter with bruschetta and cured meats" cx="200" cy="762" r="84" fill="url(#platter-tones)"/>
    <circle cx="413" cy="759" r="88" fill="var(--white)"/>
    <circle class="photo-produce" role="img" aria-label="Photo of mixed fresh vegetables and fruit" cx="413" cy="759" r="82" fill="url(#veg-tones)"/>
    <circle cx="610" cy="710" r="88" fill="var(--white)"/>
    <circle class="photo-pizza" role="img" aria-label="Photo of a tomato and basil pizza" cx="610" cy="710" r="82" fill="url(#pizza-tones)"/>
  </svg>

  <div class="brand">
    <span class="brand-name">Grubella</span>
    <span class="brand-sub">Home Delivery</span>
  </div>

  <p class="intro">Avoid the supermarkets and enjoy a unique and balanced food experience with provenance.</p>

  <p class="order">Order online at<br>
    <span class="url">www.grubellahomedelivery.example</span><br>
    <span class="note">for fast contactless next day delivery.</span>
  </p>

  <p class="body-copy about">Grubella brings you the very best producers and growers from The Garden of England to deliver you a delicious choice for all your dining needs. From fresh produce boxes, handmade picnic boxes, fresh Kentish berry boxes to the finest local beer and wines – we’ve got it covered.</p>

  <p class="body-copy green">Using environmentally conscious practices and minimal packaging, working hand in hand with reduced food miles brings you peace of mind with our efforts for a sustainable future.</p>

  <p class="promo">ENTER CODE<span class="code">LOCALTOHOME</span>AT THE CHECKOUT</p>

  <div class="offer">
    <span class="offer-big first">ENJOY 25%</span>
    <span class="offer-line">OFF ALL YOUR ORDERS IN</span>
    <span class="offer-big">JULY</span>
  </div>

  <div class="cta">
    <span class="cta-head">SHOP NOW AT</span>
    <span class="cta-url">www.grubellahomedelivery.example</span>
    <span class="cta-call">OR CALL ONE OF OUR FRIENDLY TEAM AT THE FARM ON</span>
    <span class="cta-phone">01632 960418.</span>
  </div>
</main>
</body>
</html>
```